Automotive parts Package (box) design

We are developing a new packaging concept for our automotive service and suspension parts line. I will share 2–3 sample designs—some from other brands and some AI‑generated—and we need a designer to create a unified, original design direction based on these references.

We already have an established brand name, KEM, along with a logo. The logo may be updated or redesigned, but the brand name KEM must remain.

- The project includes creating the full packaging design for our product boxes, developing or refining the logo if needed.

-Then, after choosing the design, we will apply the same design to 8 boxes with small customisation for each box to match the product.

- The box die-lines will be provided by us.

Attached are a few sample designs. We need you to develop three or more new designs in a similar style. If you have additional creative concepts beyond these references, you are welcome to include them. The only fixed requirement is that the brand name KEM must remain unchanged in all proposed designs.

Box files such as PNG, PDF (ready-to-print file) and Ai (Editable/ Source file) and fonts with 3D mockup images at the end of the project must be given to us.

Target Market(s)

Car spare parts shops

Industry/Entity Type

Auto Parts

Requirements
Must have
• Our brand name KEM
Nice to have
• Package similar to big auto parts suppliers such as PLW, VARNE

```html
<!DOCTYPE html>
<html lang="en">
<head>
<meta charset="utf-8">
<title>KEM Ball Joint Box</title>
<link href="https://fonts.googleapis.com/css2?family=Oswald:wght@600;700&family=Roboto:wght@500;700;900&display=swap" rel="stylesheet">
<style>
  :root{
    --bg:#f6f3f2;
    --black:#141414;
    --panel:#1b1b1b;
    --red:#c8283a;
    --white:#ffffff;
    --rule:#3a3a3a;
  }
  *{margin:0;padding:0;box-sizing:border-box}
  html,body{width:1200px;height:960px;overflow:hidden;background:var(--bg)}
  body{position:relative;font-family:'Roboto',sans-serif;color:var(--white)}
  .panel{position:absolute;background:var(--panel);overflow:hidden}
  .panel-top{left:60px;top:60px;width:760px;height:260px}
  .panel-front{left:60px;top:340px;width:760px;height:520px}
  .panel-side{left:840px;top:340px;width:300px;height:520px}

  .brand{position:absolute;display:flex;flex-direction:column;align-items:flex-start}
  .brand-name{font-family:'Oswald',sans-serif;font-weight:700;color:var(--white);line-height:1;letter-spacing:6px}
  .brand-sub{font-family:'Roboto',sans-serif;font-weight:700;color:var(--white);letter-spacing:4px;border-top:1.5px solid var(--red);padding-top:4px;margin-top:4px}

  .tagline{position:absolute;font-family:'Roboto',sans-serif;font-weight:700;text-transform:uppercase;line-height:1.2}
  .tagline .t-red{color:var(--red)}

  /* top flap */
  .panel-top .brand{left:80px;top:40px}
  .panel-top .brand-name{font-size:56px}
  .panel-top .brand-sub{font-size:9px}
  .panel-top .tagline{left:80px;top:150px;font-size:14px;border-top:1.5px solid var(--red);padding-top:10px;width:250px}
  .top-band{position:absolute;right:0;top:40px;width:440px;height:180px}
  .top-title{position:absolute;right:40px;top:95px;font-family:'Oswald',sans-serif;font-weight:700;font-style:italic;font-size:44px;color:var(--red);letter-spacing:1px}
  .top-sub{position:absolute;right:52px;top:158px;font-size:12px;font-weight:900;color:var(--black);letter-spacing:.5px}

  /* front face */
  .panel-front .brand{left:60px;top:44px}
  .panel-front .brand-name{font-size:78px}
  .panel-front .brand-sub{font-size:11px;letter-spacing:5px}
  .front-band{position:absolute;left:0;top:196px;width:460px;height:230px}
  .front-title{position:absolute;left:56px;top:210px;font-family:'Oswald',sans-serif;font-weight:700;font-size:74px;line-height:1;color:var(--white)}
  .front-sub{position:absolute;left:56px;top:300px;font-size:20px;font-weight:700;line-height:1.25;text-transform:uppercase}
  .speed-lines{position:absolute;left:40px;top:400px}
  .product-photo{position:absolute;left:320px;top:300px;width:260px;height:190px;border-radius:10px;
    background:radial-gradient(ellipse at 55% 50%,#8a8884 0%,#4f4d4a 55%,rgba(27,27,27,0) 80%)}
  .panel-front .tagline{right:50px;top:60px;text-align:right;font-size:20px}
  .tag-rule{position:absolute;right:0;top:120px}

  .features{position:absolute;right:40px;top:156px;width:130px;display:flex;flex-direction:column;align-items:center;gap:12px}
  .feature{display:flex;flex-direction:column;align-items:center;gap:6px}
  .feature-label{font-size:12px;font-weight:700;text-align:center;line-height:1.2;text-transform:uppercase}
  .features .feature + .feature{border-top:1px solid var(--rule);padding-top:10px;width:100%}

  /* side face */
  .panel-side .brand{left:40px;top:30px}
  .panel-side .brand-name{font-size:54px}
  .panel-side .brand-sub{font-size:8px}
  .side-band{position:absolute;left:0;top:120px;width:300px;height:76px;background:var(--red)}
  .side-title{position:absolute;left:40px;top:126px;font-family:'Oswald',sans-serif;font-weight:700;font-size:48px;line-height:1;color:var(--white)}
  .side-sub{position:absolute;left:40px;top:206px;font-size:11px;font-weight:700;text-transform:uppercase}
  .side-features{position:absolute;left:14px;top:246px;width:272px;display:flex;justify-content:space-between}
  .side-features .feature{width:86px}
  .side-features .feature-label{font-size:9px}
  .label-area{position:absolute;left:0;bottom:0;width:300px;height:150px;background:var(--white)}
</style>
</head>
<body>

<section class="panel panel-top">
  <div class="brand">
    <span class="brand-name">KEM</span>
    <span class="brand-sub">AUTOMOTIVE COMPONENTS</span>
  </div>
  <p class="tagline">Built for safety<br><span class="t-red">Designed for performance</span></p>
  <svg class="top-band" viewBox="0 0 440 180" aria-hidden="true">
    <polygon points="0,0 440,0 440,180 40,180" fill="var(--red)"/>
    <polygon points="20,70 440,70 440,140 34,140" fill="var(--white)"/>
  </svg>
  <span class="top-title">BALL JOINT</span>
  <span class="top-sub">STEERING &amp; SUSPENSION PARTS</span>
</section>

<section class="panel panel-front">
  <div class="brand">
    <span class="brand-name">KEM</span>
    <span class="brand-sub">AUTOMOTIVE COMPONENTS</span>
  </div>

  <svg class="front-band" viewBox="0 0 460 230" aria-hidden="true">
    <polygon points="0,0 460,0 330,230 0,230" fill="var(--red)"/>
  </svg>
  <h1 class="front-title">BALL JOINT</h1>
  <p class="front-sub">Steering &amp;<br>Suspension parts</p>
  <svg class="speed-lines" width="220" height="30" viewBox="0 0 220 30" aria-hidden="true">
    <line x1="40" y1="6" x2="160" y2="6" stroke="var(--black)" stroke-width="3"/>
    <line x1="20" y1="20" x2="200" y2="20" stroke="var(--black)" stroke-width="3"/>
  </svg>

  <div class="product-photo" role="img" aria-label="Photo of a tie rod end and a lower ball joint"></div>

  <p class="tagline"><span class="t-red">Built for safety</span><br>Designed for performance</p>
  <svg class="tag-rule" width="260" height="16" viewBox="0 0 260 16" aria-hidden="true">
    <polygon points="10,0 260,0 260,16 0,16" fill="var(--red)"/>
  </svg>

  <div class="features">
    <div class="feature">
      <svg width="52" height="52" viewBox="0 0 60 60" aria-hidden="true">
        <circle cx="30" cy="30" r="27" fill="none" stroke="var(--white)" stroke-width="2"/>
        <circle cx="30" cy="27" r="11" fill="none" stroke="var(--red)" stroke-width="2"/>
        <polygon points="25,25 35,25 30,32" fill="none" stroke="var(--red)" stroke-width="1.5"/>
        <polyline points="24,36 22,44 26,42 28,46" fill="none" stroke="var(--red)" stroke-width="1.5"/>
        <polyline points="36,36 38,44 34,42 32,46" fill="none" stroke="var(--red)" stroke-width="1.5"/>
      </svg>
      <span class="feature-label">Premium<br>quality</span>
    </div>
    <div class="feature">
      <svg width="52" height="52" viewBox="0 0 60 60" aria-hidden="true">
        <circle cx="30" cy="30" r="27" fill="none" stroke="var(--white)" stroke-width="2"/>
        <path d="M30 15 L42 20 V30 C42 38 36 43 30 45 C24 43 18 38 18 30 V20 Z" fill="none" stroke="var(--red)" stroke-width="2"/>
        <circle cx="35" cy="37" r="5" fill="var(--red)"/>
        <path d="M35 40 V34 M33 36 L35 34 L37 36" stroke="var(--white)" stroke-width="1.2" fill="none"/>
      </svg>
      <span class="feature-label">High<br>durability</span>
    </div>
    <div class="feature">
      <svg width="52" height="52" viewBox="0 0 60 60" aria-hidden="true">
        <circle cx="30" cy="30" r="27" fill="none" stroke="var(--white)" stroke-width="2"/>
        <path d="M18 40 A12 12 0 0 1 42 40" fill="none" stroke="var(--red)" stroke-width="2"/>
        <line x1="30" y1="40" x2="36" y2="32" stroke="var(--red)" stroke-width="2"/>
        <path d="M20 20 H32 M23 25 H38" stroke="var(--red)" stroke-width="1.5"/>
      </svg>
      <span class="feature-label">Smooth<br>performance</span>
    </div>
  </div>
</section>

<section class="panel panel-side">
  <div class="brand">
    <span class="brand-name">KEM</span>
    <span class="brand-sub">AUTOMOTIVE COMPONENTS</span>
  </div>
  <div class="side-band"></div>
  <h2 class="side-title">BALL JOINT</h2>
  <p class="side-sub">Steering &amp; suspension parts</p>
  <div class="side-features">
    <div class="feature">
      <svg width="44" height="44" viewBox="0 0 60 60" aria-hidden="true">
        <circle cx="30" cy="30" r="27" fill="none" stroke="var(--white)" stroke-width="2"/>
        <circle cx="30" cy="27" r="11" fill="none" stroke="var(--red)" stroke-width="2"/>
        <polygon points="25,25 35,25 30,32" fill="none" stroke="var(--red)" stroke-width="1.5"/>
      </svg>
      <span class="feature-label">Premium<br>quality</span>
    </div>
    <div class="feature">
      <svg width="44" height="44" viewBox="0 0 60 60" aria-hidden="true">
        <circle cx="30" cy="30" r="27" fill="none" stroke="var(--white)" stroke-width="2"/>
        <path d="M30 15 L42 20 V30 C42 38 36 43 30 45 C24 43 18 38 18 30 V20 Z" fill="none" stroke="var(--red)" stroke-width="2"/>
      </svg>
      <span class="feature-label">High<br>durability</span>
    </div>
    <div class="feature">
      <svg width="44" height="44" viewBox="0 0 60 60" aria-hidden="true">
        <circle cx="30" cy="30" r="27" fill="none" stroke="var(--white)" stroke-width="2"/>
        <path d="M18 40 A12 12 0 0 1 42 40" fill="none" stroke="var(--red)" stroke-width="2"/>
        <line x1="30" y1="40" x2="36" y2="32" stroke="var(--red)" stroke-width="2"/>
      </svg>
      <span class="feature-label">Smooth<br>performance</span>
    </div>
  </div>
  <div class="label-area"></div>
</section>

</body>
</html>
```